Graphic Design for Free Community Event

We need a graphic created for a community event that is aimed at families with younger children called Totz Jam. This is a free event and has a fair/carnival feel to it with rides, games, and food. I need the graphic to be flexible enough to be able to be modified and used in a variety of ways on different print and digital marketing materials. I also need the centerpiece of the design to be an event logo that can be used as a standalone element.

The overall feel needs to be fun and friendly with a slightly modern edge to it. Attached are some images used in past events. These are for reference only and do not need to be simulated or used in the final product.

Target Market(s)

Families with children

Industry/Entity Type

Church

Font styles to use
Sans Serif

Requirements
Must have
• - Logo that incorporates the event name- Event Date: August 20 - Event Time: 10am - 2pm - Church name and logo incorporated: Bright Harbor Community Church (see attached logo files)
Nice to have
• - Bright colors- Flexible design elements that are interchangeable and scalable for use of the design in different layouts across different mediums and materials.
Should not have
• - Any references or images related to drugs, alcohol, tobacco, or other subjects that would be inappropriate for children.

```html
<!DOCTYPE html>
<html lang="en">
<head>
<meta charset="utf-8">
<title>Totz Jam – Bright Harbor Community Church</title>
<link rel="stylesheet" href="https://fonts.googleapis.com/css2?family=Fredoka:wght@500;600;700&display=swap">
<style>
  :root {
    --cream: #fdf6c8;
    --white: #ffffff;
    --ink: #231f20;
    --red: #e31e2d;
    --red-dark: #b8182a;
    --purple: #7b3f92;
    --url-purple: #6a2c91;
    --magenta: #e3087f;
    --blue: #1f9bd8;
    --navy: #2b3990;
    --teal: #2bbfb0;
    --yellow: #fbbf16;
    --pink: #ec1c63;
    --orange: #f7941d;
    --green: #27ae4a;
    --peach: #fbd2b5;
    --pale-blue: #c9e7f7;
    --pale-pink: #f8c6d7;
  }
  * { margin: 0; padding: 0; box-sizing: border-box; }
  html, body { width: 810px; height: 1200px; overflow: hidden; }
  body { font-family: "Fredoka", sans-serif; }
  .poster {
    position: relative;
    width: 810px;
    height: 1200px;
    overflow: hidden;
    background: linear-gradient(180deg, var(--cream) 0%, #fffbe6 45%, var(--white) 70%);
  }
  .backdrop { position: absolute; inset: 0; }
  .church {
    position: absolute;
    left: 256px;
    top: 82px;
    display: flex;
    align-items: center;
    gap: 14px;
  }
  .church-dot {
    width: 66px; height: 66px; border-radius: 50%;
    background: var(--ink);
    flex: none;
  }
  .church-name {
    color: var(--ink);
    font-weight: 500;
    font-size: 25px;
    line-height: 1.05;
    text-transform: uppercase;
  }
  .free-label {
    position: absolute;
    left: 273px; width: 260px;
    top: 193px;
    text-align: center;
    color: var(--white);
    font-weight: 700;
    font-size: 48px;
    letter-spacing: 1px;
  }
  .event-title {
    position: absolute;
    left: 0; right: 0;
    top: 252px;
    text-align: center;
    font-weight: 700;
    font-size: 140px;
    line-height: 1;
    letter-spacing: 2px;
    white-space: nowrap;
  }
  .event-title span {
    -webkit-text-stroke: 10px var(--ink);
    paint-order: stroke fill;
    text-shadow: 4px 7px 0 var(--ink);
  }
  .t1 { color: var(--green); }
  .o  { color: var(--yellow); }
  .t2 { color: var(--magenta); }
  .z  { color: var(--blue); }
  .j  { color: var(--purple); }
  .a  { color: var(--orange); }
  .m  { color: var(--teal); }
  .event-date, .event-time {
    position: absolute; left: 0; right: 0;
    text-align: center;
    color: var(--red);
    font-weight: 700;
    line-height: 1;
  }
  .event-date { top: 396px; font-size: 50px; }
  .event-time { top: 455px; font-size: 54px; }
  .feature-label {
    position: absolute;
    transform: translateX(-50%);
    color: var(--white);
    font-weight: 700;
    font-size: 36px;
    line-height: 1;
    -webkit-text-stroke: 6px var(--navy);
    paint-order: stroke fill;
    white-space: nowrap;
  }
  .label-rides { left: 198px; top: 774px; -webkit-text-stroke-color: var(--purple); }
  .label-inflatables { left: 609px; top: 783px; }
  .label-food { left: 400px; top: 972px; -webkit-text-stroke-color: var(--red-dark); }
  .event-url {
    position: absolute; left: 0; right: 0;
    top: 1068px;
    text-align: center;
    color: var(--url-purple);
    font-weight: 600;
    font-size: 37px;
  }
</style>
</head>
<body>
<main class="poster">
  <svg class="backdrop" width="810" height="1200" viewBox="0 0 810 1200" aria-hidden="true">
    <defs>
      <linearGradient id="grad-rides" x1="0" y1="0" x2="0" y2="1">
        <stop offset="0" stop-color="#e3087f"/><stop offset="1" stop-color="#7b3399"/>
      </linearGradient>
      <linearGradient id="grad-food" x1="0" y1="0" x2="0" y2="1">
        <stop offset="0" stop-color="#ec1c24"/><stop offset="1" stop-color="#c21d3a"/>
      </linearGradient>
      <linearGradient id="grad-inflatables" x1="0" y1="0" x2="0" y2="1">
        <stop offset="0" stop-color="#21a7e0"/><stop offset="1" stop-color="#2b3990"/>
      </linearGradient>
    </defs>
    <!-- scattered dots -->
    <g class="confetti-dots">
      <circle cx="124" cy="81" r="39" fill="var(--teal)"/>
      <circle cx="407" cy="15" r="22" fill="var(--yellow)"/>
      <circle cx="759" cy="51" r="54" fill="var(--purple)"/>
      <circle cx="629" cy="62" r="20" fill="var(--pink)"/>
      <circle cx="757" cy="163" r="20" fill="var(--teal)"/>
      <circle cx="614" cy="179" r="14" fill="var(--yellow)"/>
      <circle cx="17" cy="181" r="24" fill="var(--purple)"/>
      <circle cx="201" cy="432" r="22" fill="var(--red)"/>
      <circle cx="365" cy="554" r="17" fill="var(--pink)"/>
      <circle cx="451" cy="603" r="11" fill="var(--purple)"/>
      <circle cx="603" cy="489" r="10" fill="var(--teal)"/>
      <circle cx="728" cy="523" r="42" fill="var(--yellow)"/>
      <circle cx="106" cy="906" r="29" fill="var(--yellow)"/>
      <circle cx="736" cy="962" r="29" fill="var(--pink)"/>
      <circle cx="51" cy="1144" r="37" fill="var(--teal)"/>
      <circle cx="611" cy="1148" r="22" fill="var(--purple)"/>
      <circle cx="302" cy="1190" r="30" fill="var(--pink)"/>
      <circle cx="770" cy="1117" r="19" fill="var(--yellow)"/>
      <circle cx="613" cy="232" r="4" fill="var(--blue)"/>
      <circle cx="578" cy="408" r="4" fill="var(--pink)"/>
      <circle cx="659" cy="174" r="8" fill="none" stroke="var(--orange)" stroke-width="2"/>
      <circle cx="37" cy="317" r="8" fill="none" stroke="var(--blue)" stroke-width="2"/>
      <circle cx="610" cy="394" r="8" fill="none" stroke="var(--blue)" stroke-width="2"/>
      <circle cx="181" cy="209" r="4" fill="none" stroke="var(--pink)" stroke-width="1.5"/>
      <circle cx="731" cy="251" r="4" fill="none" stroke="var(--pink)" stroke-width="1.5"/>
      <circle cx="730" cy="368" r="4" fill="none" stroke="var(--orange)" stroke-width="1.5"/>
    </g>
    <!-- confetti slivers -->
    <g class="confetti-slivers">
      <polygon points="104,188 166,218 158,208" fill="var(--orange)"/>
      <polygon points="680,210 668,243 662,237" fill="var(--pink)"/>
      <polygon points="30,280 92,290 70,306" fill="#f487b6"/>
      <polygon points="33,423 78,398 72,410" fill="var(--orange)"/>
      <polygon points="705,398 758,438 745,428" fill="var(--blue)"/>
      <polygon points="720,305 780,294 748,312" fill="var(--orange)"/>
    </g>
    <!-- soft backing circles -->
    <circle cx="124" cy="523" r="62" fill="var(--purple)"/>
    <circle cx="404" cy="695" r="54" fill="var(--peach)"/>
    <circle cx="631" cy="881" r="74" fill="var(--pale-blue)"/>
    <circle cx="251" cy="958" r="61" fill="var(--pale-pink)"/>
    <circle cx="64" cy="776" r="24" fill="var(--teal)"/>
    <!-- feature circles -->
    <circle cx="198" cy="685" r="157" fill="url(#grad-rides)" role="img" aria-label="Ferris wheel ride icon"/>
    <circle cx="400" cy="888" r="157" fill="url(#grad-food)" role="img" aria-label="Food truck icon"/>
    <circle cx="609" cy="726" r="157" fill="url(#grad-inflatables)" role="img" aria-label="Bounce castle icon"/>
    <!-- FREE ribbon -->
    <polygon class="free-ribbon" points="273,192 533,186 508,218 528,252 284,255 303,222" fill="var(--red)"/>
  </svg>

  <div class="church">
    <span class="church-dot"></span>
    <span class="church-name">Bright Harbor<br>Community Church</span>
  </div>

  <div class="free-label">FREE</div>

  <h1 class="event-title"><span class="t1">T</span><span class="o">O</span><span class="t2">T</span><span class="z">Z</span> <span class="j">J</span><span class="a">A</span><span class="m">M</span></h1>

  <p class="event-date">August 20</p>
  <p class="event-time">10am - 2pm</p>

  <span class="feature-label label-rides">RIDES</span>
  <span class="feature-label label-inflatables">INFLATABLES</span>
  <span class="feature-label label-food">FOOD</span>

  <p class="event-url">www.brightharborchurch.org/totzjam</p>
</main>
</body>
</html>
```